Crestline Supply Software Design

I would like a construction focused flyer design (if possible, inline with the current design esthetic from my website www.crsupsw.com), 1 standard US page (8.5x11"), front and back, full color glossy. I want a design I can use for multiple software partners, so I want the ability to edit the template that is created. This can be full page or folded- whatever you think is best.Attached are my logos, and a current flyer. I want to use the logo and the color scheme- feel free to make the logo colors even brighter. Everything else can be changed! Any additional graphics should be software or construction focused.

Target Market(s)

Electrical, Mechanical and Plumbing Construction Companies, specifically their accounting, IT, purchasing staff.

Font styles to use
Sans Serif

Colors
6b449b
9ccb3b

Requirements
Must have
• Lots of construction oriented graphics. Discreet boxes for text that can be changed in using photoshop or Illustrator products CS6 or earlier.
• Designs should be:
• - B2B focused
• - merge technology and construction
• - Show how technology can save time
• - Automation is a good thing
Should not have
• Be saved in a format that can not be used by CS6 or earlier.

```html
<!DOCTYPE html>
<html lang="en">
<head>
<meta charset="utf-8">
<title>Crestline Supply Software – Flyer</title>
<link href="https://fonts.googleapis.com/css2?family=Roboto+Condensed:wght@400;700&display=swap" rel="stylesheet">
<style>
:root{
  --green:#4db848;
  --purple:#6b4c9e;
  --purple-deep:#5b3e90;
  --black:#000;
  --white:#fff;
  --ink:#111;
  --stage:#1f5a85;
}
*{box-sizing:border-box;margin:0;padding:0}
html,body{width:1200px;height:1200px;overflow:hidden;background:var(--stage)}
body{position:relative;font-family:"Roboto Condensed",sans-serif;color:var(--ink)}
.flyer{position:absolute;left:136px;top:0;width:1039px;height:1344px;background:var(--white);transform:scale(.8929);transform-origin:0 0;overflow:hidden}
.header{position:absolute;left:0;top:0;width:100%;height:258px;background:linear-gradient(var(--green) 0 129px,var(--white) 129px 131px,var(--purple) 131px)}
.brand-box,.offer-box{position:absolute;top:28px;height:218px;background:var(--white);border:3px solid var(--black)}
.brand-box{left:37px;width:528px}
.brand-mark{position:absolute;left:16px;top:16px;width:190px;height:180px;background:var(--black)}
.brand-name{position:absolute;left:234px;top:24px;font-weight:700;color:var(--purple);font-size:44px;line-height:1.08;text-transform:uppercase}
.offer-box{left:587px;width:402px;padding:48px 0 0 19px}
.offer-title{font-weight:700;font-size:42px;line-height:1}
.offer-sub{font-size:23px;line-height:1.22;margin-top:6px}
.offer-tag{font-weight:700;font-size:21px;margin-top:10px}
.intro{position:absolute;left:55px;top:274px;width:945px;font-size:17.5px;line-height:1.3}
.intro b{font-weight:700}
.tiles{position:absolute;left:39px;top:379px;width:956px;height:359px;display:flex;gap:6px}
.tile{flex:1;border-radius:8px;color:var(--white);padding:22px 18px 0;font-size:16.5px;line-height:1.24}
.tile h2{font-size:20px;font-weight:700;margin-bottom:11px}
.tile p+p{margin-top:20px}
.tile--green{background:var(--green)}
.tile--purple{background:var(--purple)}
.tile--black{background:var(--black)}
.feature{position:absolute;left:50px;width:960px}
.feature-icon{position:absolute;left:0;top:0;width:93px;height:93px;border-radius:50%;background:var(--purple);display:flex;align-items:center;justify-content:center}
.feature h3{position:absolute;left:110px;top:-6px;font-size:25px;font-weight:700;color:var(--purple);white-space:nowrap}
.feature p{position:absolute;left:118px;top:26px;width:850px;font-size:16.5px;line-height:1.24}
.footer-rule{position:absolute;left:0;top:1262px;width:100%;height:8px;background:var(--green)}
.footer{position:absolute;left:0;top:1270px;width:100%;height:74px;background:var(--black);color:var(--white);font-size:25px;display:flex;align-items:center;padding-left:59px;white-space:pre}
</style>
</head>
<body>
<div class="flyer">
  <header class="header">
    <div class="brand-box">
      <div class="brand-mark"></div>
      <div class="brand-name">Crestline<br>Supply<br>Software</div>
    </div>
    <div class="offer-box">
      <div class="offer-title">PROVOICE!</div>
      <div class="offer-sub">Purchase Order Creation and Vendor Automation PLUS Invoice Matching!</div>
      <div class="offer-tag">Why frustrate when you can automate!</div>
    </div>
  </header>

  <p class="intro"><b>CRESTLINE SUPPLY SOFTWARE</b> offers three levels of automation and procurement expertise across the acquisition life cycle. CRESTLINE SUPPLY offers a full-fledged items based materials system, an automated purchase order acknowledgement system, and an invoice matching suite to take the guess work out of vendor payments- and all of this works with your accounting system.</p>

  <section class="tiles">
    <div class="tile tile--green">
      <h2>SWIFT PURCHASE:</h2>
      <p>Will give you access to a price analysis and purchase order management system that puts you in total control of your all your projects’ materials.</p>
      <p>SWIFT PURCHASE is an ideal solution for purchase agents who want an easy, yet comprehensive, way to quickly generate and manage purchases, analyze material usage, and compare supplier pricing. SWIFT PURCHASE provides all this power and will seamlessly upload committed costs and material into your accounting system.</p>
    </div>
    <div class="tile tile--purple">
      <h2>SWIFT ORDER CONFIRMATION</h2>
      <p>Could you avoid a lot of manual typing if you could automatically pull your vendor’s data from your orders for you to review and push into your accounting software? Then SWIFT ORDER is your tool of choice.</p>
      <p>For a fraction of the cost of headcount, you can automate your PO’s from any vendor and upload that data, without errors, straight into your accounting system.</p>
    </div>
    <div class="tile tile--black">
      <h2>SWIFT INVOICE:</h2>
      <p>Are your Accounts Payable staff tired of trying to match the PO to the invoice and figuring out what the Purchasing team did? Well there’s an app for that- with SWIFT INVOICE.</p>
      <p>Crestline Supply Software can be the interface with your vendor to pull down the data from their ERP to load into yours, all the while reducing errors, time to enter, and automating matching.</p>
    </div>
  </section>

  <section class="feature" style="top:758px">
    <div class="feature-icon"></div>
    <h3 style="left:110px">Comprehensive Materials Management</h3>
    <p>SWIFT PURCHASE has comprehensive materials management capabilities, starting with useful features such as backorder control. You will never have to wonder where material is any longer. With SWIFT PURCHASE once a PO is created you can specify the delivery date needed, promised, scheduled, and actual. With SWIFT PURCHASE you will also know where your materials are so that you can avoid those costly slowdowns due to incorrect materials</p>
  </section>

  <section class="feature" style="top:889px">
    <div class="feature-icon">
      <svg width="56" height="56" viewBox="0 0 56 56" fill="none" stroke="#fff" stroke-width="3" stroke-linejoin="round"><path d="M18 4h22l10 10v34H26"/><path d="M40 4v10h10"/><path d="M4 24h6l5 14h16l4-11H12"/><circle cx="17" cy="44" r="3"/><circle cx="29" cy="44" r="3"/></svg>
    </div>
    <h3 style="left:120px">Purchase Order History- Good Information</h3>
    <p>Do you wish you had “Backorder Reports” or accurate “Job Material Usage Reports” but have you held off because of the time it takes to enter the information? Congratulations you do not have to wait any longer SWIFT ORDER CONFIRMATION is the answer. With just a couple of clicks your orders will be entered just as if you had taken the time to type them in one line at a time. With SWIFT ORDER CONFIRMATION you can easily keep up with all the daily orders AND get the benefit of the information too.</p>
  </section>

  <section class="feature" style="top:1030px">
    <div class="feature-icon">
      <svg width="62" height="56" viewBox="0 0 62 56" fill="none" stroke="#fff" stroke-width="3.5" stroke-linejoin="round"><rect x="3" y="26" width="10" height="24" rx="3" fill="#fff"/><path d="M19 26l10-14c2-4 3-8 3-10 5 0 7 4 6 9l-2 9h15c4 0 6 3 5 6l-4 18c-1 4-3 6-7 6H19z"/></svg>
    </div>
    <h3 style="left:118px">Easy to Use</h3>
    <p>All THREE PRODUCTS- SWIFT ORDER CONFIRMATION, SWIFT INVOICE, SWIFT PURCHASE are easy to use, most users require a maximum of 10 minutes of training and they are processing their orders. Most products install in minutes and save you hours of processing time. CRESTLINE SUPPLY makes managing and documenting your purchasing quick and easy, giving you greater control over material expenditures</p>
  </section>

  <section class="feature" style="top:1154px">
    <div class="feature-icon">
      <svg width="58" height="54" viewBox="0 0 58 54" fill="none" stroke="#fff" stroke-width="3.5" stroke-linejoin="round"><path d="M54 4L4 28l16 6 6 16z"/><path d="M54 4L20 34"/></svg>
    </div>
    <h3 style="left:115px">Unparalleled Speed in processing</h3>
    <p>Nothing is faster or more accurate than CRESTLINE SUPPLY. When you open the system you will be presented with a list of current orders or invoices to process. All you have to do is confirm the matching purchase lines and within a few clicks your order or invoice is uploaded into accounting.</p>
  </section>

  <div class="footer-rule"></div>
  <footer class="footer">www.crsupsw.com  |  Crestline Supply Software, Inc. PO Box 480212 Denton, TX  76201</footer>
</div>
</body>
</html>
```